Exciting New Health Brand. Needs packaging design

We need a label and packaging design for a US based colloidal Silver water product due to launch shortly.
we like the vibe and feel of this: https://www.shopvarlo.example/Pure-Brightwell-Dropper-Top-Regal-Tonic/dp/K48TRW2MPL/ref=sr_1_1_sspa?ie=UTF8&qid=1520284298&sr=8-1-spons&keywords=regal+tonic+colloidal+tonic&psc=1 though would need to make it look different

Target Market(s)

people who like natural health, and alternative health such as yoga, reiki etc

Industry/Entity Type

Health And Wellness

Font styles to use
Other font styles liked:
• open minded

Colors

Designer to choose colors to be used in the design.

Requirements
Must have
• Vibrant feel.Brand name is fernwell vitals
Nice to have
• quite open minded
Should not have
• mustn't have cheap animated look

```html
<!DOCTYPE html>
<html lang="en">
<head>
<meta charset="utf-8">
<title>Fernwell Vitals – Immune Support Packaging</title>
<link rel="stylesheet" href="https://fonts.googleapis.com/css2?family=Oswald:wght@400;600;700&display=swap">
<style>
  :root {
    --page: #ffffff;
    --frame: #9a9a9a;
    --frame-light: #cfcfcf;
    --frame-dark: #6f6f6f;
    --sky-light: #bfe6f7;
    --sky: #5fb8e6;
    --water: #2f8fc9;
    --water-deep: #1d6c9e;
    --ribbon-light: #ffd36a;
    --ribbon: #f5a623;
    --ribbon-edge: #e07f10;
    --ribbon-text: #2433a8;
    --base-orange: #f07822;
    --accent-red: #e0462a;
    --ink-dark: #2b2b2b;
    --ink-white: #ffffff;
    --panel-white: #ffffff;
    --panel-blue: #3aa4e4;
    --amber-top: #3a2a20;
    --amber-mid: #5a4232;
    --amber-low: #4a3526;
  }
  * { box-sizing: border-box; margin: 0; padding: 0; }
  html, body { width: 1200px; height: 890px; overflow: hidden; background: var(--page); }
  body { font-family: "Oswald", "Arial Narrow", sans-serif; position: relative; }

  /* Carton front */
  .carton-front {
    position: absolute; left: 200px; top: 75px; width: 360px; height: 740px;
    display: flex; flex-direction: column;
    box-shadow: 0 10px 30px rgba(0,0,0,.18);
  }
  .frame-band {
    height: 22px;
    background: linear-gradient(180deg, var(--frame-light), var(--frame) 50%, var(--frame-dark));
  }
  .carton-scene { position: relative; flex: 1; overflow: hidden; }
  .scene-art {
    position: absolute; inset: 0;
    background: linear-gradient(180deg, var(--sky-light) 0%, var(--sky) 30%, var(--water) 65%, var(--water-deep) 100%);
  }

  /* Brand name in place of the mark */
  .brand-name {
    position: absolute; left: 0; right: 0;
    display: flex; align-items: center; justify-content: center; gap: 10px;
    font-weight: 700; font-size: 38px; line-height: 1; color: var(--ink-dark);
  }
  .brand-dot {
    width: 20px; height: 20px; border-radius: 50%; background: var(--panel-white); flex: none;
  }
  .carton-scene .brand-name { top: 150px; }

  .bottle-art {
    position: absolute; left: 112px; top: 262px; width: 138px; height: 340px;
    border-radius: 40px 40px 14px 14px;
    background: linear-gradient(180deg, var(--amber-top), var(--amber-mid) 40%, var(--amber-low));
  }
  .immune-ribbon {
    position: absolute; left: 20px; top: 380px; width: 320px; height: 60px;
    background: linear-gradient(180deg, var(--ribbon-light), var(--ribbon) 55%, var(--ribbon-edge));
    transform: rotate(-12deg);
    display: flex; align-items: center; justify-content: center;
    font-weight: 700; font-size: 32px; color: var(--ribbon-text); letter-spacing: 1px;
  }
  .carton-base {
    height: 102px; background: var(--base-orange); color: var(--ink-white);
    text-align: center; padding-top: 28px; font-weight: 600; line-height: 1.25;
  }
  .base-title { font-size: 17px; }
  .base-volume { font-size: 15px; }

  /* Bottle label */
  .bottle-label {
    position: absolute; left: 640px; top: 165px; width: 360px; height: 560px;
    border: 10px solid var(--frame);
    box-shadow: 0 10px 30px rgba(0,0,0,.18);
    overflow: hidden;
  }
  .bottle-label .scene-art {
    background: linear-gradient(180deg, var(--sky-light) 0%, var(--sky) 35%, var(--water) 75%, var(--water-deep) 100%);
  }
  .bottle-label .brand-name { top: 130px; }
  .label-info {
    position: absolute; left: 55px; right: 55px; bottom: 22px; height: 170px;
    border-radius: 14px; background: var(--panel-blue); border: 4px solid var(--panel-white);
    text-align: center; padding-top: 22px;
  }
  .info-kind { color: var(--ink-white); font-size: 15px; font-weight: 600; }
  .info-claim {
    margin: 14px -10px 0; background: var(--panel-white); border-radius: 6px;
    color: var(--accent-red); font-size: 26px; font-weight: 700; padding: 4px 0;
  }
  .info-volume {
    color: var(--ink-dark); background: var(--panel-white); margin: 10px 10px 0;
    border-radius: 0 0 10px 10px; font-size: 13px; font-weight: 600; padding: 6px 0;
  }
</style>
</head>
<body>
  <section class="carton-front">
    <div class="frame-band"></div>
    <div class="carton-scene">
      <div class="scene-art" role="img" aria-label="Water splash over mountain lake and waterfalls"></div>
      <div class="brand-name"><span class="brand-dot"></span>FERNWELL VITALS</div>
      <div class="bottle-art" role="img" aria-label="Amber dropper bottle with product label"></div>
      <div class="immune-ribbon">IMMUNE SUPPORT</div>
    </div>
    <div class="frame-band"></div>
    <div class="carton-base">
      <div class="base-title">DIETARY SUPPLEMENT</div>
      <div class="base-volume">10 PPM / 8 FL OZ. / 236 ML</div>
    </div>
  </section>

  <section class="bottle-label">
    <div class="scene-art" role="img" aria-label="Water splash and mountain scene behind label text"></div>
    <div class="brand-name"><span class="brand-dot"></span>FERNWELL VITALS</div>
    <div class="label-info">
      <div class="info-kind">DIETARY SUPPLEMENT</div>
      <div class="info-claim">IMMUNE SUPPORT</div>
      <div class="info-volume">10 PPM / 8 FL OZ. / 236 ML</div>
    </div>
  </section>
</body>
</html>
```